Small Artisan Bakery Needs a new Bread Bag Label

I'm looking for a new bread bag label design for our artisan bakery. I have attached photos of our current logo (we will be using this in the label) and pictures of our bread bag. For this project we will focus on one of our bread (100% Rye) however I would like the final final to be in a format I can edit for other bread types.

We are thinking that each bread bag will have 2 labels, our logo on top of the bread bag window (as shown in the attached photos) and simple bread description below the window.

We typically use Copperplate font however we are open to ideas as long as it keeps in alignment with our logo.

*Also note, we will not be printing the labels directly on the bag. The designs will be printed as labels that will be stuck on each bag. I would like to have the final designs formatted in a way that makes it simple to have printed at a standard printing shop.

The bag is 9.5" long, 5" wide.

The length fro the bottom of the bag window to the bottom of the bag is 2".

Top of the bag to top of the window is a little over 4".

Since these labels will be printed on label paper and manually stuck on the bag I would like them to not be take up up the whole space above or below the bag window. If the label design comes to the edge of the bag it will be very difficult to physically stick the label on the bag straight.

Thanks

Hi, The bag is 9.5" long, 5" wide. The length fro the bottom of the bag window to the bottom of the bag is 2". Top of the bag to top of the window is a little over 4". Since these labels will be printed on label paper and manually stuck on the bag I would like them to not be take up up the whole space above or below the bag window. If the label design comes to the edge of the bag it will be very difficult to physically stick the label on the bag straight. Thanks

```html
<!DOCTYPE html>
<html lang="en">
<head>
<meta charset="utf-8">
<title>Birch Creek Bread – 100% Rye Bag Labels</title>
<link rel="stylesheet" href="https://fonts.googleapis.com/css2?family=Cinzel:wght@700&family=Tinos&display=swap">
<style>
  :root {
    --page: #efece4;
    --olive: #4b5a1f;
    --label-ground: #e6e9df;
    --pattern-tone: #dfe6d6;
    --frame-line: #5a5f2c;
    --ribbon-dark: #4e7a1e;
    --ribbon-light: #7fae3a;
    --ribbon-text: #ffffff;
    --brand-ink: #2d2a17;
    --body-ink: #1e1e1e;
  }
  * { box-sizing: border-box; margin: 0; padding: 0; }
  html, body { width: 930px; height: 1200px; overflow: hidden; }
  body { background: var(--page); position: relative; }

  .label {
    position: absolute;
    background: var(--olive);
    border-radius: 34px;
  }
  .label__ground {
    position: absolute;
    background: var(--label-ground);
    border-radius: 22px;
    overflow: hidden;
  }
  .label__frame {
    position: absolute;
    border: 2px dashed var(--frame-line);
  }

  /* Logo label (top) */
  .logo-label { left: 294px; top: 176px; width: 428px; height: 424px; }
  .logo-label .label__ground { left: 20px; top: 20px; right: 20px; bottom: 20px; }
  .wheat-field {
    position: absolute; inset: 0;
    background: radial-gradient(circle at 50% 45%, var(--label-ground), var(--pattern-tone));
  }
  .logo-label .label__frame { left: 6px; top: 8px; right: 6px; bottom: 8px; }

  .brand {
    position: absolute;
    left: 0; right: 0; top: 78px;
    text-align: center;
    font-family: "Cinzel", serif;
    font-weight: 700;
    color: var(--brand-ink);
    line-height: 1.1;
  }
  .brand__mark {
    display: block;
    width: 30px; height: 30px;
    margin: 0 auto 10px;
    border-radius: 50%;
    background: var(--brand-ink);
  }
  .brand__name { display: block; font-size: 30px; letter-spacing: 2px; }
  .brand__word { display: block; font-size: 40px; letter-spacing: 4px; }

  .variety-ribbon {
    position: absolute;
    left: 66px; top: 262px;
    width: 260px; height: 58px;
  }

  /* Description label (bottom) */
  .info-label { left: 306px; top: 975px; width: 362px; height: 155px; }
  .info-label .label__ground { left: 14px; top: 14px; right: 14px; bottom: 14px; border-radius: 16px; }
  .info-label .label__frame { left: 5px; top: 5px; right: 5px; bottom: 5px; }
  .description {
    position: absolute; inset: 0;
    display: flex; flex-direction: column; justify-content: center; gap: 6px;
    text-align: center;
    font-family: "Tinos", "Times New Roman", serif;
    font-size: 11.5px;
    line-height: 1.3;
    color: var(--body-ink);
  }
</style>
</head>
<body>

  <section class="label logo-label">
    <div class="label__ground">
      <div class="wheat-field" role="img" aria-label="Scattered pale green wheat stalk pattern"></div>
      <div class="label__frame"></div>

      <div class="brand">
        <span class="brand__mark"></span>
        <span class="brand__name">BIRCH CREEK</span>
        <span class="brand__word">BREAD</span>
      </div>

      <svg class="variety-ribbon" viewBox="0 0 260 58" aria-label="100% Rye">
        <defs>
          <linearGradient id="ribbonFill" x1="0" y1="0" x2="0" y2="1">
            <stop offset="0" stop-color="var(--ribbon-light)"/>
            <stop offset="1" stop-color="var(--ribbon-dark)"/>
          </linearGradient>
        </defs>
        <g transform="rotate(-14 130 29)">
          <rect x="8" y="10" width="244" height="40" fill="url(#ribbonFill)" stroke="#e9f0d8" stroke-width="2"/>
          <text x="130" y="38" text-anchor="middle" fill="var(--ribbon-text)"
                font-family="Cinzel, serif" font-weight="700" font-size="22" letter-spacing="2">100% RYE</text>
        </g>
      </svg>
    </div>
  </section>

  <section class="label info-label">
    <div class="label__ground">
      <div class="label__frame"></div>
      <div class="description">
        <p>100% Rye Bread-<br>naturally leavened and fermented<br>100% Lithuanian rye bread.</p>
        <p>100% organic rye flour,<br>110 year old organic rye culture,<br>and grey Celtic sea salt</p>
      </div>
    </div>
  </section>

</body>
</html>
```